Book Cover on Entrepreneurship for Eye Doctors

Book Title: The Lens Clinic Founder: How to launch your practice with flair
Author: Morvan Tessaleq, Optom, MBA, DBA, EIC
I need a Book Cover with the following descriptions:
Topic: the book topic is entrepreneurship knowledge for eye care professionals.
The book's audience: eye care professionals who you know as Opticians, who sell eyeglasses and sunglasses;
Optometrists, test eyes, fit contact lenses, and prescribe medication
Ophthalmologists, perform eye surgery
More about the audience:
1- Young eye care professionals who don’t know about entrepreneurship and those who are stuck in the 9-to-5 job;
2- This is the first book written on entrepreneurship with eye care professionals in mind.
3- Private practice owners the established business guys who are looking to grow their business;
4- Many eye care professionals are MBA holders they may have learned a little bit about entrepreneurship during their MBA studies.
Use the sample cover above and the suggestions that follow as a guide:
1- The cover should be very simple leaving an empty space somewhere to sign the book;
2- The Title and author name should use a modern font;
3- The cover should provide info about what's inside the book through illustrations, for example:
a- Gears: illustrating entrepreneur growth mindset (or anything more explicit)
b- Spectacles, sunglasses, lenses, eye drops, or any other eye care-related correction tools illustrating eye care (or anything more explicit)
c- Symbols illustrating ideas, opportunity, and profit, like money, charts, light bulbs, brain, and coins,...(or anything more explicit)
d- Entrepreneurship illustrated by Briefcase, tie, suit,... (or anything more explicit)

The rest is your creativity and imagination interplay.

Target Market(s)

Eye care professionals: Opticians, Optometrists, Ophthalmologists, Eye Care Administrators, Students in eye specialties.

Industry/Entity Type

eye care

Requirements
Must have
• 1- The cover should be very simple leaving an empty space somewhere to sign the book; 2- The Title and author name should use a modern font; 3- The cover should provide info about what's inside the book through illustrations, for example: a- Gears: illustrating entrepreneur growth mindset (or anything more explicit) b- Spectacles, sunglasses, lenses, eye drops, or any other eye care-related correction tools illustrating eye care (or anything more explicit) c- Symbols illustrating ideas, opportunity, and profit, like money, charts, light bulbs, brain, and coins,...(or anything more explicit) d- Entrepreneurship illustrated by Briefcase, tie, suit,... (or anything more explicit)

```html
<!DOCTYPE html>
<html lang="en">
<head>
<meta charset="utf-8">
<title>The Lens Clinic Founder – Book Cover</title>
<link rel="stylesheet" href="https://fonts.googleapis.com/css2?family=Marcellus&family=Marcellus+SC&family=Crimson+Text&family=Cormorant+Garamond:ital,wght@1,500&display=swap">
<style>
  :root{
    --navy:#163f70;
    --teal:#3fb2b1;
    --teal-light:#8fd3d8;
    --white:#ffffff;
    --page:#e9eaec;
    --paper-shadow:rgba(20,40,70,.18);
  }
  *{box-sizing:border-box;margin:0;padding:0}
  html,body{width:1200px;height:1200px;overflow:hidden;background:var(--page)}
  .wrap{position:absolute;left:55px;top:185px;width:1090px;height:830px;display:flex;box-shadow:0 10px 30px var(--paper-shadow)}

  /* ---------- Back cover ---------- */
  .back{position:relative;width:520px;height:830px;background:var(--navy);overflow:hidden}
  .back-title{position:absolute;top:48px;left:0;width:100%;text-align:center;font-family:"Marcellus",serif}
  .title-the{display:flex;align-items:center;justify-content:center;gap:8px;font-family:"Marcellus",serif}
  .title-the .rule{height:3px;width:70px}
  .back .title-the{color:var(--white);font-size:34px;line-height:1}
  .back .title-the .rule{background:var(--white);width:80px;height:2px;margin-top:-22px}
  .back .word-lens{color:var(--teal);font-size:112px;line-height:.9}
  .back .word-clinic{color:var(--teal);font-size:58px;line-height:1}
  .back .word-founder{color:var(--white);font-size:30px;line-height:1.2;letter-spacing:1px}

  .back-blurb{position:absolute;top:300px;left:32px;right:32px;height:270px;overflow:hidden;font-family:"Crimson Text",serif;color:var(--teal);font-size:13.5px;line-height:17px;text-align:justify}
  .back-author{position:absolute;top:582px;left:0;width:100%;text-align:center;font-family:"Marcellus SC",serif;color:var(--white);font-size:20px}
  .author-photo{position:absolute;top:622px;left:32px;width:108px;height:186px;background:var(--white)}
  .author-bio{position:absolute;top:620px;left:156px;right:32px;height:120px;overflow:hidden;font-family:"Crimson Text",serif;color:var(--teal);font-size:13.5px;line-height:17px;text-align:justify}
  .back-band{position:absolute;left:0;bottom:0;width:100%;height:82px;background:var(--teal)}
  .code-box{position:absolute;right:32px;bottom:18px;width:140px;height:104px;background:var(--white)}

  /* ---------- Spine ---------- */
  .spine{position:relative;width:50px;height:830px;background:var(--white);border-left:1px solid #d5dbe3;border-right:1px solid #d5dbe3}
  .spine-text{position:absolute;top:26px;left:0;width:100%;height:690px;writing-mode:vertical-rl;display:flex;align-items:center;justify-content:space-between;font-family:"Marcellus SC",serif;color:var(--navy)}
  .spine-title{font-size:21px;letter-spacing:1px}
  .spine-title .accent{color:var(--teal)}
  .spine-author{font-size:15px;font-style:normal}
  .spine-band{position:absolute;left:0;bottom:0;width:100%;height:110px;background:var(--navy)}

  /* ---------- Front cover ---------- */
  .front{position:relative;width:520px;height:830px;background:var(--white);overflow:hidden}
  .front-title{position:absolute;top:72px;left:0;width:100%;text-align:center;font-family:"Marcellus",serif}
  .front .title-the{color:var(--navy);font-size:52px;line-height:1}
  .front .title-the .rule{background:var(--navy);width:118px;height:2px;margin-top:-30px}
  .front .word-lens{color:var(--teal);font-size:168px;line-height:.86;margin-top:8px}
  .front .word-clinic{color:var(--teal);font-size:92px;line-height:1}
  .front .word-founder{color:var(--navy);font-size:56px;line-height:1.15;letter-spacing:4px}

  .subtitle{position:absolute;top:488px;left:90px;right:90px;text-align:center;font-family:"Cormorant Garamond",serif;font-style:italic;font-weight:500;color:var(--navy);font-size:22px;padding:12px 0}
  .subtitle::before,.subtitle::after{content:"";position:absolute;left:0;right:0;height:1px;background:linear-gradient(90deg,transparent,var(--teal) 50%,transparent)}
  .subtitle::before{top:0}
  .subtitle::after{bottom:0}

  .front-art{position:absolute;top:590px;left:46px;width:428px;height:130px;border-radius:6px;background:linear-gradient(180deg,#f4fafb 0%,#c9ebec 55%,#8fd3d8 100%)}
  .front-band{position:absolute;left:0;bottom:0;width:100%;height:110px;background:var(--navy);display:flex;align-items:center;justify-content:center}
  .front-author{font-family:"Marcellus SC",serif;color:var(--white);font-size:22px;letter-spacing:.3px}
</style>
</head>
<body>
<main class="wrap">

  <section class="back" aria-label="Back cover">
    <header class="back-title">
      <div class="title-the"><span class="rule"></span>THE<span class="rule"></span></div>
      <div class="word-lens">LENS</div>
      <div class="word-clinic">CLINIC</div>
      <div class="word-founder">FOUNDER</div>
    </header>
    <div class="back-blurb">
      <p>Lorem ipsum dolor sit amet, consectetuer adipiscing elit, sed diam nonummy nibh euismod tincidunt ut laoreet dolore magna aliquam erat volutpat. Ut wisi enim ad minim veniam, quis nostrud exerci tation ullamcorper suscipit lobortis nisl ut aliquip ex ea commodo consequat. Duis autem vel eum iriure dolor in hendrerit in vulputate velit esse molestie consequat, vel illum dolore eu feugiat nulla facilisis at vero eros et accumsan et iusto odio dignissim qui blandit praesent luptatum zzril delenit augue duis dolore te feugait nulla facilisi.</p>
      <p>Lorem ipsum dolor sit amet, cons ectetuer adipiscing elit, sed diam nonummy nibh euismod tincidunt ut laoreet dolore magna aliquam erat volutpat. Ut wisi enim ad minim veniam, quis nostrud exerci tation ullamcorper suscipit lobortis nisl ut aliquip ex ea commodo consequat.</p>
      <p>Lorem ipsum dolor sit amet, consectetuer adipiscing elit, sed diam nonummy nibh euismod tincidunt ut laoreet dolore magna aliquam erat volutpat. Ut wisi enim ad minim veniam, quis nostrud exerci tation ullamcorper suscipit lobortis nisl ut aliquip ex ea commodo consequat.</p>
    </div>
    <p class="back-author">Morvan Tessaleq, Optom, MBA, DBA, EIC</p>
    <div class="author-photo" role="img" aria-label="Author portrait placeholder"></div>
    <div class="author-bio">
      <p>Lorem ipsum dolor sit amet, consectetuer adipiscing elit, sed diam nonummy nibh euismod tincidunt ut laoreet dolore magna aliquam erat volutpat. Ut wisi enim ad minim veniam, quis nostrud exerci tation ullamcorper suscipit lobortis nisl ut aliquip ex ea commodo consequat. Duis autem vel eum iriure dolor in hendrerit in vulputate velit esse molestie consequat.</p>
    </div>
    <div class="back-band"></div>
    <div class="code-box"></div>
  </section>

  <section class="spine" aria-label="Spine">
    <div class="spine-text">
      <span class="spine-title">The <span class="accent">Lens Clinic</span> Founder</span>
      <span class="spine-author">Morvan Tessaleq, Optom, MBA, DBA, EIC</span>
    </div>
    <div class="spine-band"></div>
  </section>

  <section class="front" aria-label="Front cover">
    <header class="front-title">
      <div class="title-the"><span class="rule"></span>THE<span class="rule"></span></div>
      <h1 class="word-lens">LENS</h1>
      <div class="word-clinic">CLINIC</div>
      <div class="word-founder">FOUNDER</div>
    </header>
    <p class="subtitle">How to launch your practice with flair</p>
    <div class="front-art" role="img" aria-label="Illustration of small eye care professionals around giant spectacles, an eye chart, eye drops and a large eye"></div>
    <footer class="front-band">
      <p class="front-author">Morvan Tessaleq, Optom, MBA, DBA, EIC</p>
    </footer>
  </section>

</main>
</body>
</html>
```